Thistle Croft B&B Business Card

This beautiful high-class B&B is looking for a business card that stands out from the rest. They are in the middle of the countryside, have chickens, geese and a dog. They also love bumble bees.

I was maybe thinking a rustic drawing / print of a bumble bee and a sketch of the house, I am not sure.. I quite like the feel of this... http://www.fenwick-mill.co.uk/

Industry/Entity Type

Business

Contact Information for Business Card

Thistle Croft
Bed & Breakfast
Holtwick, Brackenford, Ambershire, BF4 7QR
01632 961847 | www.thistlecroft.co.uk

```html
<!DOCTYPE html>
<html lang="en">
<head>
<meta charset="utf-8">
<title>Thistle Croft B&amp;B Business Card</title>
<link href="https://fonts.googleapis.com/css2?family=Lato:wght@400;700&display=swap" rel="stylesheet">
<style>
  :root {
    --navy: #1e3a73;
    --green: #2f7d32;
    --ink: #222;
    --paper: #ffffff;
    --backdrop: #e9e7e3;
    --stone-light: #f2f1ee;
    --stone-mid: #c9c6bf;
    --stone-dark: #9a968e;
  }
  * { box-sizing: border-box; margin: 0; padding: 0; }
  html, body { width: 1200px; height: 912px; overflow: hidden; }
  body {
    background: var(--backdrop);
    font-family: 'Lato', sans-serif;
    position: relative;
  }
  .card {
    position: absolute;
    left: 280px;
    width: 640px;
    height: 400px;
    background: var(--paper);
    box-shadow: 0 6px 18px rgba(0,0,0,0.18);
    overflow: hidden;
  }
  .card--front { top: 40px; }
  .card--back { top: 472px; }

  .house-sketch {
    position: absolute;
    inset: 0;
    background: linear-gradient(160deg, var(--stone-light) 0%, var(--stone-mid) 45%, var(--stone-dark) 75%, var(--stone-light) 100%);
  }
  .house-sketch::after {
    content: "";
    position: absolute;
    inset: 0;
    background: linear-gradient(90deg, rgba(255,255,255,0) 50%, rgba(255,255,255,0.85) 100%);
  }

  .brand { position: absolute; color: var(--navy); }
  .brand__tagline {
    font-weight: 400;
    text-transform: uppercase;
    letter-spacing: 0.5px;
  }
  .brand__name {
    font-weight: 400;
    line-height: 1;
    white-space: nowrap;
  }
  .card--front .brand { right: 36px; bottom: 70px; text-align: right; }
  .card--front .brand__tagline { color: var(--green); font-size: 22px; margin-bottom: 4px; }
  .card--front .brand__name { font-size: 62px; }

  .card--back .brand { left: 56px; top: 150px; }
  .card--back .brand__tagline { color: var(--ink); font-size: 15px; margin-bottom: 4px; }
  .card--back .brand__name { font-size: 40px; }

  .divider {
    position: absolute;
    left: 372px;
    top: 120px;
    width: 1px;
    height: 130px;
    background: var(--navy);
  }
  .contact {
    position: absolute;
    left: 400px;
    top: 150px;
    list-style: none;
    color: var(--ink);
    font-size: 16px;
  }
  .contact li { display: flex; align-items: center; gap: 10px; margin-bottom: 12px; }
  .contact svg { width: 14px; height: 14px; fill: var(--navy); flex: none; }

  .address-band {
    position: absolute;
    left: 0; right: 0; bottom: 0;
    height: 48px;
    background: var(--navy);
    color: var(--paper);
    font-size: 18px;
    display: flex;
    align-items: center;
    justify-content: center;
    letter-spacing: 0.3px;
  }
</style>
</head>
<body>
  <section class="card card--front">
    <div class="house-sketch" role="img" aria-label="Pencil sketch of the stone farmhouse with gate and arched window"></div>
    <div class="brand">
      <p class="brand__tagline">Bed &amp; Breakfast</p>
      <p class="brand__name">Thistle Croft</p>
    </div>
  </section>

  <section class="card card--back">
    <div class="brand">
      <p class="brand__tagline">Bed &amp; Breakfast</p>
      <p class="brand__name">Thistle Croft</p>
    </div>
    <div class="divider"></div>
    <ul class="contact">
      <li>
        <svg viewBox="0 0 24 24" aria-hidden="true"><path d="M6.6 10.8a15.1 15.1 0 0 0 6.6 6.6l2.2-2.2a1 1 0 0 1 1-.25 11.4 11.4 0 0 0 3.6.57 1 1 0 0 1 1 1V20a1 1 0 0 1-1 1A17 17 0 0 1 3 4a1 1 0 0 1 1-1h3.5a1 1 0 0 1 1 1c0 1.25.2 2.45.57 3.57a1 1 0 0 1-.25 1z"/></svg>
        01632 961847
      </li>
      <li>
        <svg viewBox="0 0 24 24" aria-hidden="true"><circle cx="12" cy="12" r="10"/><path d="M2 12h20M12 2c3 3 3 17 0 20M12 2c-3 3-3 17 0 20" stroke="#fff" stroke-width="1.5" fill="none"/></svg>
        www.thistlecroft.co.uk
      </li>
    </ul>
    <div class="address-band">Holtwick, Brackenford, Ambershire, BF4 7QR</div>
  </section>
</body>
</html>
```